Sports nutritional supplement brand*

We need to design an integrated packaging for a sports nutritional supplement brand containing more than 30 products The design of the packaging consists of two parts, half in black color, fixed in all types, and the other half is variable. I sent you pictures containing some beautiful ideas that suit what I think of. The design must contain a place for the taste image, such as chocolate, strawberry, banana, orange, grape, watermelon The company name must be clearly visible in the middle and the location of the code and barcode

Target Market(s)

the whole world

Industry/Entity Type

Entrepreneur

Font styles to use
Decorative

Colors

Designer to choose colors to be used in the design.

Requirements
Must have
• The project consists of several types of supplements. I need each type to be different from the other in terms of a color that is constant, such as the black color and the half of the box is color changing, for example the box is made of black and red and the second box is black and yellow and the colors must be bright and 3D
Nice to have
• The outer box will be white and the box will be completely wrapped from the head neck down, not around the box There should be a small box design, a large protein box, and a protein pouch bag
Should not have

```html
<!DOCTYPE html>
<html lang="en">
<head>
<meta charset="utf-8">
<title>FITCORE Sports Nutritional Supplement Packaging</title>
<link href="https://fonts.googleapis.com/css2?family=Russo+One&family=Oswald:wght@500;600&display=swap" rel="stylesheet">
<style>
  :root {
    --bg: #eeeeee;
    --black: #141414;
    --cap: #1c1c1c;
    --silver: #d9d9d9;
    --ink: #161616;
    --choco: #4a2a1c;
    --choco-dark: #2e1810;
    --straw: #d8262c;
    --straw-dark: #a81a1f;
    --banana: #f2c21a;
    --banana-dark: #d9a40c;
    --white: #ffffff;
    --pill: #e6e6e6;
  }
  * { margin: 0; padding: 0; box-sizing: border-box; }
  html, body { width: 1200px; height: 1000px; overflow: hidden; background: var(--bg); }
  .canvas { position: relative; width: 1200px; height: 1000px; background: var(--bg); }

  .pack { position: absolute; }
  .chocolate { --accent: var(--choco); --accent-dark: var(--choco-dark); }
  .strawberry { --accent: var(--straw); --accent-dark: var(--straw-dark); }
  .banana { --accent: var(--banana); --accent-dark: var(--banana-dark); }

  /* jars */
  .jar__cap {
    position: absolute; left: 4%; width: 92%; border-radius: 8px 8px 3px 3px;
    background: repeating-linear-gradient(90deg, var(--cap) 0 3px, #2a2a2a 3px 5px);
  }
  .jar__body {
    position: absolute; left: 0; width: 100%; border-radius: 16px 16px 14px 14px;
    background: var(--black); overflow: hidden;
  }

  /* pouches */
  .pouch__body {
    position: absolute; inset: 0; background: var(--black); overflow: hidden;
    border-radius: 6px 6px 10px 10px;
  }
  .pouch__zip { position: absolute; left: 0; right: 0; top: 9%; height: 2px; background: var(--accent-dark); opacity: .7; }

  /* colour band: --band-l / --band-r are the band depths at left and right edges */
  .band {
    position: absolute; inset: 0;
    background: var(--accent);
    clip-path: polygon(0 0, 100% 0, 100% var(--band-r), 0 var(--band-l));
  }
  .band__edge {
    position: absolute; inset: 0;
    background: var(--silver);
    clip-path: polygon(0 var(--band-l), 100% var(--band-r), 100% calc(var(--band-r) + 3px), 0 calc(var(--band-l) + 3px));
  }
  .brand {
    position: absolute;
    transform: rotate(-9deg); transform-origin: left bottom;
    white-space: nowrap;
  }
  .brand__name {
    font-family: "Russo One", sans-serif; color: var(--white); line-height: 1; display: block;
  }
  .brand__tag {
    font-family: "Oswald", sans-serif; font-weight: 500; color: var(--ink);
    display: block; margin-top: 2px; line-height: 1.1; letter-spacing: .3px;
  }

  .flavour-art { position: absolute; border-radius: 40% 45% 35% 40%; }
  .chocolate .flavour-art { background: radial-gradient(circle at 45% 50%, #6b3a22, #3a1d10 70%); }
  .strawberry .flavour-art { background: radial-gradient(circle at 45% 55%, #f4f0ea 0 30%, #d42a2a 55%, #8e1416 85%); }
  .banana .flavour-art { background: radial-gradient(circle at 45% 55%, #f4f0ea 0 28%, #f2c21a 55%, #b58a08 85%); }

  .stats {
    position: absolute; right: 5%; width: 13%;
    background: var(--pill); border-radius: 999px;
    display: flex; flex-direction: column; align-items: center; justify-content: space-around;
    padding: 6px 0; font-family: "Oswald", sans-serif; text-align: center;
  }
  .stat__value { color: var(--accent); font-weight: 600; line-height: 1; display: block; }
  .stat__label { color: #555; font-size: 3px; line-height: 1.1; display: block; text-transform: uppercase; }

  .flavour-label {
    position: absolute; left: 50%; transform: translateX(-50%);
    background: var(--accent); color: var(--white); white-space: nowrap;
    font-family: "Oswald", sans-serif; font-weight: 500; text-transform: uppercase;
    border-radius: 999px; padding: 2px 10px;
  }
  .jar .flavour-label { font-size: 8px; }
  .pouch .flavour-label { font-size: 11px; padding: 4px 14px; }
</style>
</head>
<body>
<main class="canvas">

  <!-- jars -->
  <section class="pack jar chocolate" style="left:380px; top:145px; width:148px; height:280px;">
    <div class="jar__cap" style="top:0; height:56px;"></div>
    <div class="jar__body" style="top:55px; height:225px; --band-l:95px; --band-r:72px;">
      <div class="band"></div><div class="band__edge"></div>
      <div class="brand" style="left:10px; bottom:136px;">
        <span class="brand__name" style="font-size:22px;">FITCORE</span>
        <span class="brand__tag" style="font-size:6px;">Sports Nutritional Supplement</span>
      </div>
      <div class="flavour-art" role="img" aria-label="Chocolate pieces" style="left:24px; top:110px; width:92px; height:70px;"></div>
      <div class="stats" style="top:100px; height:80px;">
        <span><span class="stat__value" style="font-size:8px;">50</span><span class="stat__label">Servings</span></span>
        <span><span class="stat__value" style="font-size:8px;">27</span><span class="stat__label">Protein grams</span></span>
        <span><span class="stat__value" style="font-size:8px;">500</span><span class="stat__label">Grams</span></span>
      </div>
      <div class="flavour-label" style="top:198px; background:transparent; color:var(--silver);">Chocolates &amp; Cream</div>
    </div>
  </section>

  <section class="pack jar banana" style="left:697px; top:152px; width:141px; height:283px;">
    <div class="jar__cap" style="top:0; height:60px;"></div>
    <div class="jar__body" style="top:58px; height:225px; --band-l:92px; --band-r:70px;">
      <div class="band"></div><div class="band__edge"></div>
      <div class="brand" style="left:10px; bottom:139px;">
        <span class="brand__name" style="font-size:21px;">FITCORE</span>
        <span class="brand__tag" style="font-size:6px;">Sports Nutritional Supplement</span>
      </div>
      <div class="flavour-art" role="img" aria-label="Bananas" style="left:20px; top:100px; width:80px; height:85px;"></div>
      <div class="stats" style="top:100px; height:80px;">
        <span><span class="stat__value" style="font-size:8px;">50</span><span class="stat__label">Servings</span></span>
        <span><span class="stat__value" style="font-size:8px;">27</span><span class="stat__label">Protein grams</span></span>
        <span><span class="stat__value" style="font-size:8px;">500</span><span class="stat__label">Grams</span></span>
      </div>
      <div class="flavour-label" style="top:197px;">Bananas &amp; Cream</div>
    </div>
  </section>

  <section class="pack jar strawberry" style="left:528px; top:123px; width:169px; height:327px;">
    <div class="jar__cap" style="top:0; height:66px;"></div>
    <div class="jar__body" style="top:64px; height:263px; --band-l:105px; --band-r:78px;">
      <div class="band"></div><div class="band__edge"></div>
      <div class="brand" style="left:12px; bottom:164px;">
        <span class="brand__name" style="font-size:26px;">FITCORE</span>
        <span class="brand__tag" style="font-size:7px;">Sports Nutritional Supplement</span>
      </div>
      <div class="flavour-art" role="img" aria-label="Strawberries" style="left:28px; top:115px; width:100px; height:105px;"></div>
      <div class="stats" style="top:125px; height:95px;">
        <span><span class="stat__value" style="font-size:9px;">50</span><span class="stat__label">Servings</span></span>
        <span><span class="stat__value" style="font-size:9px;">27</span><span class="stat__label">Protein grams</span></span>
        <span><span class="stat__value" style="font-size:9px;">500</span><span class="stat__label">Grams</span></span>
      </div>
      <div class="flavour-label" style="top:232px;">Strawberries &amp; Cream</div>
    </div>
  </section>

  <!-- pouches -->
  <section class="pack pouch chocolate" style="left:348px; top:548px; width:172px; height:337px;">
    <div class="pouch__body" style="--band-l:140px; --band-r:113px;">
      <div class="band"></div><div class="band__edge"></div><div class="pouch__zip"></div>
      <div class="brand" style="left:12px; bottom:203px;">
        <span class="brand__name" style="font-size:28px;">FITCORE</span>
        <span class="brand__tag" style="font-size:8px;">Sports Nutritional Supplement</span>
      </div>
      <div class="flavour-art" role="img" aria-label="Chocolate pieces with milk splash" style="left:14px; top:160px; width:120px; height:115px;"></div>
      <div class="stats" style="top:170px; height:100px;">
        <span><span class="stat__value" style="font-size:10px;">50</span><span class="stat__label">Servings</span></span>
        <span><span class="stat__value" style="font-size:10px;">27</span><span class="stat__label">Protein grams</span></span>
        <span><span class="stat__value" style="font-size:10px;">500</span><span class="stat__label">Grams</span></span>
      </div>
      <div class="flavour-label" style="top:302px; background:transparent; color:var(--silver);">Bananas &amp; Cream</div>
    </div>
  </section>

  <section class="pack pouch banana" style="left:712px; top:548px; width:181px; height:337px;">
    <div class="pouch__body" style="--band-l:140px; --band-r:111px;">
      <div class="band"></div><div class="band__edge"></div><div class="pouch__zip"></div>
      <div class="brand" style="left:12px; bottom:203px;">
        <span class="brand__name" style="font-size:29px;">FITCORE</span>
        <span class="brand__tag" style="font-size:8px;">Sports Nutritional Supplement</span>
      </div>
      <div class="flavour-art" role="img" aria-label="Bananas with milk splash" style="left:14px; top:155px; width:125px; height:125px;"></div>
      <div class="stats" style="top:180px; height:95px;">
        <span><span class="stat__value" style="font-size:10px;">50</span><span class="stat__label">Servings</span></span>
        <span><span class="stat__value" style="font-size:10px;">27</span><span class="stat__label">Protein grams</span></span>
        <span><span class="stat__value" style="font-size:10px;">500</span><span class="stat__label">Grams</span></span>
      </div>
      <div class="flavour-label" style="top:302px;">Bananas &amp; Cream</div>
    </div>
  </section>

  <section class="pack pouch strawberry" style="left:503px; top:525px; width:220px; height:380px;">
    <div class="pouch__body" style="--band-l:160px; --band-r:125px;">
      <div class="band"></div><div class="band__edge"></div><div class="pouch__zip"></div>
      <div class="brand" style="left:16px; bottom:227px;">
        <span class="brand__name" style="font-size:34px;">FITCORE</span>
        <span class="brand__tag" style="font-size:10px;">Sports Nutritional Supplement</span>
      </div>
      <div class="flavour-art" role="img" aria-label="Strawberries with cream splash" style="left:22px; top:175px; width:150px; height:145px;"></div>
      <div class="stats" style="top:205px; height:115px;">
        <span><span class="stat__value" style="font-size:12px;">50</span><span class="stat__label">Servings</span></span>
        <span><span class="stat__value" style="font-size:12px;">27</span><span class="stat__label">Protein grams</span></span>
        <span><span class="stat__value" style="font-size:12px;">500</span><span class="stat__label">Grams</span></span>
      </div>
      <div class="flavour-label" style="top:340px;">Strawberries &amp; Cream</div>
    </div>
  </section>

</main>
</body>
</html>
```